Retractable Banner Design for Retail Shopping Event

I need a design for a 33” by 86” retractable banner. It should have my logo at the top (the largest element of the design) and the banner should also include my website and Instagram handle:
www.verikamode.com
@verikamode
I have included product pictures in the brief that can be used. I also included different versions of my logo file, including AI. I need the file to be ready to upload to my printer.
My store is an upscale women’s boutique. I am also attaching designs I have selected in the past to give an idea of my aesthetic.

```html
<!DOCTYPE html>
<html lang="en">
<head>
<meta charset="utf-8">
<title>Verika Mode – Sip &amp; Shop Banner</title>
<link href="https://fonts.googleapis.com/css2?family=Arimo:wght@400;700&family=Playfair+Display:ital,wght@0,700;1,600&display=swap" rel="stylesheet">
<style>
  :root {
    --stage: #b6babd;
    --blush: #e7d0c7;
    --charcoal: #58595a;
    --ink: #4f4f50;
    --cocoa: #5b3b36;
    --gold: #c9a44a;
    --leopard: #c9a267;
    --bag: #cfaea3;
    --plush: #d9bfc0;
    --suede: #9d8593;
  }
  * { box-sizing: border-box; margin: 0; padding: 0; }
  html, body { width: 1200px; height: 1200px; overflow: hidden; }
  body { background: var(--stage); position: relative; font-family: "Arimo", Arial, sans-serif; }

  .banner {
    position: absolute; left: 380px; top: 27px;
    width: 440px; height: 1146px;
    background: var(--blush); overflow: hidden;
  }
  .brand {
    position: absolute; left: 0; right: 0; top: 82px;
    text-align: center;
    font-family: "Playfair Display", Georgia, serif; font-weight: 700;
    font-size: 46px; letter-spacing: 2px; color: var(--charcoal); line-height: 1.1;
  }
  .event-band {
    position: absolute; left: 0; right: 0; top: 241px; height: 78px;
    background: var(--charcoal);
    display: flex; align-items: center; justify-content: center;
  }
  .event-title {
    font-family: "Playfair Display", Georgia, serif; font-style: italic; font-weight: 600;
    font-size: 38px; color: var(--blush); letter-spacing: 0.5px;
  }
  .event-details, .invite, .contact {
    position: absolute; right: 48px; text-align: right;
    color: var(--ink); text-transform: uppercase; font-size: 16px; line-height: 19px;
  }
  .event-details { top: 355px; }
  .invite { top: 428px; }
  .contact { top: 864px; text-transform: none; font-size: 15px; line-height: 21px; }

  .teaser {
    position: absolute; left: 60px; width: 320px; top: 702px;
    text-align: center; color: var(--cocoa); font-size: 20px; line-height: 25px;
  }

  .photo { position: absolute; }
  .photo-tray {
    left: -40px; top: 370px; width: 185px; height: 302px; border-radius: 50%;
    background: radial-gradient(ellipse at 40% 50%, #d8b57c 0%, var(--leopard) 60%, #a88049 100%);
  }
  .photo-bag {
    left: 270px; top: 500px; width: 190px; height: 250px; border-radius: 10px;
    background: linear-gradient(160deg, #dcc0b6, var(--bag));
    transform: rotate(12deg);
  }
  .photo-slippers {
    left: 0; top: 805px; width: 290px; height: 230px; border-radius: 0 60% 40% 0;
    background: linear-gradient(180deg, var(--plush) 0%, var(--plush) 55%, var(--suede) 100%);
  }
  .charm {
    position: absolute; width: 28px; height: 28px; border-radius: 50%;
    background: radial-gradient(circle, #e9e2d2 0%, var(--gold) 70%);
  }

  .footer-band {
    position: absolute; left: 0; right: 0; top: 1000px; bottom: 0;
    background: var(--charcoal); color: var(--blush); text-align: center;
  }
  .website { margin-top: 30px; font-size: 25px; letter-spacing: 2px; }
  .social {
    margin-top: 14px; display: flex; align-items: center; justify-content: center; gap: 8px;
    font-size: 19px;
  }
  .social-dot { width: 20px; height: 20px; border: 2px solid var(--blush); border-radius: 50%; }
</style>
</head>
<body>
  <main class="banner">
    <div class="brand">VERIKA MODE</div>

    <div class="event-band"><h1 class="event-title">Sip &amp; Shop</h1></div>

    <p class="event-details">Thursday, November 18<br>11 - 1 PM<br>Linden Avenue</p>
    <p class="invite">Come enjoy<br>sips, snacks and shopping!</p>

    <div class="photo photo-tray" role="img" aria-label="Leopard print round serving tray"></div>
    <div class="photo photo-bag" role="img" aria-label="Blush leather tote bag with embellished snake motif"></div>
    <div class="photo photo-slippers" role="img" aria-label="Pink pom-pom plush slippers"></div>

    <div class="charm" style="left:174px;top:518px;width:40px;height:40px" role="img" aria-label="Gold clover charm"></div>
    <div class="charm" style="left:198px;top:588px" role="img" aria-label="Gold clover charm"></div>
    <div class="charm" style="left:136px;top:612px;width:34px;height:34px" role="img" aria-label="Gold clover charm"></div>
    <div class="charm" style="left:342px;top:778px" role="img" aria-label="Gold clover charm"></div>
    <div class="charm" style="left:290px;top:838px" role="img" aria-label="Gold clover charm"></div>
    <div class="charm" style="left:298px;top:962px;width:32px;height:32px" role="img" aria-label="Gold clover charm"></div>
    <div class="charm" style="left:352px;top:980px;width:44px;height:44px" role="img" aria-label="Gold clover charm"></div>

    <p class="teaser">Be the first to preview our new winter collection and get an early start on your holiday gifting.</p>

    <p class="contact">Clara Benning<br>info@verikamode.com<br>555 014 2800</p>

    <footer class="footer-band">
      <p class="website">www.verikamode.com</p>
      <p class="social"><span class="social-dot"></span>@verikamode</p>
    </footer>
  </main>
</body>
</html>
```